Ridgeline Crude Advisors needs a logo design and business card layout.

RCA is a consulting firm in oil and gas, specializing in upstream engineering and field work. We provide engineering solutions for the complete wellbore cycle from casing design to flowback. This includes completion and production design. On-site job supervision and project engineering for conventional and unconventional reservoirs. Asset analysis by reviewing operational conditions of asset packages to determine value of potential acquisitions or divesture.

```html
<!DOCTYPE html>
<html lang="en">
<head>
<meta charset="utf-8">
<title>Ridgeline Crude Advisors – Business Card</title>
<link rel="stylesheet" href="https://fonts.googleapis.com/css2?family=Oswald:wght@500;600&family=Open+Sans:wght@400;600&display=swap">
<style>
  :root {
    --bg: #3b322d;
    --card-white: #f7f7f5;
    --card-dark: #2d2d2e;
    --blue: #145f9c;
    --yellow: #f6ac1c;
    --red: #ef3e23;
    --ink: #3a3a3a;
    --rule: #b9b9b9;
    --silver: #c9c9c9;
  }
  * { margin: 0; padding: 0; box-sizing: border-box; }
  html, body { width: 1200px; height: 844px; overflow: hidden; }
  body {
    background: var(--bg);
    font-family: "Open Sans", Arial, sans-serif;
    color: var(--ink);
    position: relative;
  }
  .card {
    position: absolute;
    top: 262px;
    width: 525px;
    height: 300px;
    overflow: hidden;
    box-shadow: 0 14px 30px rgba(0,0,0,.45);
  }
  .card--front { left: 55px; background: var(--card-white); }
  .card--back { left: 620px; background: var(--card-dark); }

  .stripe {
    position: absolute; left: 0; right: 0; bottom: 0; height: 11px;
    display: flex;
  }
  .stripe span { flex: 1; }
  .stripe .blue { background: var(--blue); }
  .stripe .yellow { background: var(--yellow); }
  .stripe .red { background: var(--red); }

  .brand {
    position: absolute; top: 40px; right: 60px;
    display: flex; align-items: center; gap: 10px;
  }
  .brand__mark { width: 18px; height: 18px; background: var(--red); }
  .brand__name {
    font-family: "Oswald", "Arial Narrow", sans-serif;
    font-weight: 600; font-size: 25px; letter-spacing: .5px;
    text-transform: uppercase; color: var(--blue); line-height: 1;
  }
  .brand__rule {
    position: absolute; top: 80px; right: 60px; width: 250px;
    border-top: 1px solid var(--red);
  }

  .divider {
    position: absolute; left: 30px; right: 40px; border-top: 1px solid var(--rule);
  }
  .divider--top { top: 122px; left: 130px; }
  .divider--bottom { top: 236px; }

  .person { position: absolute; left: 30px; top: 140px; }
  .person__name {
    font-family: "Oswald", "Arial Narrow", sans-serif;
    font-weight: 500; font-size: 24px; color: var(--blue);
    text-transform: uppercase; line-height: 1.05;
  }
  .person__title { font-size: 14px; line-height: 1.2; }
  .person__address { font-size: 14px; margin-top: 14px; }

  .contacts {
    position: absolute; left: 30px; top: 244px;
    font-size: 13.5px; line-height: 1.5;
  }
  .contacts b { font-weight: 600; color: var(--blue); }
  .contacts .gap { margin-left: 10px; }
  .web { color: var(--blue); }
  .web em { font-style: normal; color: var(--yellow); }
  .web i { font-style: normal; color: var(--red); }

  .back-brand {
    position: absolute; inset: 0 0 11px 0;
    display: flex; align-items: center; justify-content: center;
    font-family: "Oswald", "Arial Narrow", sans-serif;
    font-weight: 500; font-size: 30px; letter-spacing: 1px;
    text-transform: uppercase; color: var(--silver);
  }
</style>
</head>
<body>
  <section class="card card--front">
    <div class="brand">
      <span class="brand__mark"></span>
      <span class="brand__name">Ridgeline Crude Advisors</span>
    </div>
    <div class="brand__rule"></div>
    <div class="divider divider--top"></div>

    <div class="person">
      <p class="person__name">Marcus Delaney</p>
      <p class="person__title">Managing Director</p>
      <p class="person__address">12345, Address Goes Here Country Name, 123456.</p>
    </div>

    <div class="divider divider--bottom"></div>
    <div class="contacts">
      <p><b>T:</b>(044) 123 456 789 <span class="gap"><b>F:</b>(044) 123456789</span> <span class="gap"><b>M:</b>(044)123456789</span></p>
      <p><b>E:</b>info@ridgelinecrude.com <span class="gap web">www.<em>ridgelinecrude</em><i>.com</i></span></p>
    </div>

    <div class="stripe"><span class="blue"></span><span class="yellow"></span><span class="red"></span></div>
  </section>

  <section class="card card--back">
    <div class="back-brand">Ridgeline Crude Advisors</div>
    <div class="stripe"><span class="blue"></span><span class="yellow"></span><span class="red"></span></div>
  </section>
</body>
</html>
```